Process Engineering/Construction Firm wants a OneSheet targeting craft brewers in Texas

We need a OneSheet (standard letter size) that we can share with craft brewers in our state, that explains what we can do for them. This will be shared primarily via email and online. We would like to see this be fun and modern flyer while still maintaining our professional vibe. More info and logos are uploaded - please review. Also, this project could lead to more branded documents from OneSheets to letterhead. We have our website and our logo(s) and really not much else that is consistent. There is certainly opportunity to work long-term.
Updates

Please note that the website listed on the flyer should read www.harrowfieldpartnersadvisory.com. It will NOT follow the same domain name as the email address. And also, please DO NOT send me anything through the sales@hfwadvisingllc.com email address at this time. I am trying to find a brewery-specific photo to use and will upload once found. I will be uploading shortly another logo of an affiliate organization we belong to - the Lone Kettle Maltsters' League that I would like to see included on the flyer with the words, "A proud member of the Lone Kettle Maltsters' League' OR just 'Proud Member.'

Target Market(s)

Craft brewery owners in Texas

Industry/Entity Type

Engineering

Font styles to use
Sans Serif

Requirements
Must have
• We need our point of contact to list the website as well as this email: sales@hfwadvisingllc.com
• Maroon CMYK is: 32, 100, 82, 30
• We want these Brewery Specific service points included:
• • Brewhouse automation
• • Glycol systems
• • Complete line design and install
• • Packaging solutions
• • Epoxy & urethane flooring
• • New construction
• • Network of industry professionals
Nice to have
• Trendy and modern look to correlate with current craft beer logos and design trends

```html
<!DOCTYPE html>
<html lang="en">
<head>
<meta charset="utf-8">
<title>Harrowfield Partners – Brewery Services OneSheet</title>
<link rel="stylesheet" href="https://fonts.googleapis.com/css2?family=Open+Sans:wght@400;600;800&family=Roboto+Condensed:wght@700&display=swap">
<style>
  :root{
    --maroon:#8a1530;
    --maroon-deep:#5e0d20;
    --ink:#1f1f1f;
    --charcoal:#262626;
    --white:#ffffff;
    --steel-light:#c9ccce;
    --steel-dark:#6f7274;
    --backdrop:#e6e6e6;
  }
  *{margin:0;padding:0;box-sizing:border-box}
  html,body{width:1200px;height:1200px;overflow:hidden}
  body{background:var(--backdrop);position:relative;font-family:"Open Sans",Arial,sans-serif}

  .onesheet{position:absolute;left:224px;top:114px;width:750px;height:972px;overflow:hidden;background:var(--maroon)}
  .onesheet-shapes{position:absolute;inset:0}

  .brand{position:absolute;left:78px;top:62px;width:330px;text-align:center}
  .brand-name{font-family:"Open Sans",Arial,sans-serif;font-weight:800;font-size:27px;color:var(--ink);letter-spacing:-0.3px;line-height:1}
  .brand-tagline{margin-top:7px;font-weight:600;font-size:11px;letter-spacing:0.4px;color:var(--ink);border-top:2px solid var(--maroon);padding-top:4px;display:inline-block}

  .services-title{position:absolute;top:500px;left:0;width:750px;text-align:center;color:var(--white);font-weight:400;font-size:35px;letter-spacing:0.5px}

  .service{position:absolute;width:200px;text-align:center}
  .service-badge{width:78px;height:78px;margin:0 auto;border-radius:50%;background:var(--white);box-shadow:inset 0 0 0 3px var(--white),inset 0 0 0 5px var(--maroon);display:flex;align-items:center;justify-content:center}
  .service-badge svg{width:44px;height:44px;fill:none;stroke:var(--ink);stroke-width:1.6;stroke-linecap:round;stroke-linejoin:round}
  .service-label{margin-top:10px;font-family:"Roboto Condensed",Arial,sans-serif;font-weight:700;font-size:15px;line-height:21px;color:var(--white);text-transform:uppercase;letter-spacing:0.2px}

  .contact{position:absolute;left:108px;top:906px;color:var(--white);font-size:17px;line-height:21px}
  .contact-line{display:flex;align-items:center;gap:6px}
  .contact-icon{width:16px;height:16px;border-radius:50%;background:var(--maroon);display:flex;align-items:center;justify-content:center;flex:none}
  .contact-icon svg{width:10px;height:10px;fill:none;stroke:var(--white);stroke-width:1.4}
</style>
</head>
<body>
<main class="onesheet">
  <svg class="onesheet-shapes" width="750" height="972" viewBox="0 0 750 972" aria-hidden="false">
    <defs>
      <linearGradient id="facilityTone" x1="0" y1="0" x2="0" y2="1">
        <stop offset="0" stop-color="#9ea3a6"/>
        <stop offset="0.55" stop-color="#c3c6c7"/>
        <stop offset="1" stop-color="#8d8a86"/>
      </linearGradient>
      <linearGradient id="maroonTone" x1="0" y1="0" x2="1" y2="1">
        <stop offset="0" stop-color="#7a1028"/>
        <stop offset="0.5" stop-color="#931a36"/>
        <stop offset="1" stop-color="#6c0e23"/>
      </linearGradient>
    </defs>

    <rect class="facility-photo" x="0" y="0" width="750" height="520" fill="url(#facilityTone)" role="img" aria-label="Photo of a glass-walled brewery production room with a stop sign and yellow safety bollards"/>

    <path class="header-swoosh-edge" d="M0,0 H510 C470,125 360,188 200,180 C110,176 40,160 0,152 Z" fill="var(--charcoal)"/>
    <path class="header-swoosh" d="M0,0 H494 C452,112 350,172 200,166 C110,162 40,150 0,146 Z" fill="var(--white)"/>

    <path class="services-edge" d="M0,500 Q375,444 750,500 V972 H0 Z" fill="var(--charcoal)"/>
    <path class="services-panel" d="M0,512 Q375,458 750,512 V972 H0 Z" fill="url(#maroonTone)" role="img" aria-label="Maroon-tinted photo of a brewery packaging line"/>

    <path class="footer-edge" d="M0,912 C170,852 440,852 526,972 H0 Z" fill="var(--white)"/>
    <path class="footer-band" d="M0,918 C170,860 436,862 518,972 H0 Z" fill="var(--charcoal)"/>

    <g class="member-badge" role="img" aria-label="Lone Kettle Maltsters' League member badge">
      <circle cx="630" cy="118" r="86" fill="var(--charcoal)"/>
      <circle cx="630" cy="118" r="80" fill="var(--white)"/>
      <circle cx="630" cy="118" r="54" fill="var(--maroon)"/>
    </g>
  </svg>

  <div class="brand">
    <div class="brand-name">Harrowfield Partners</div>
    <div class="brand-tagline">ENGINEERING - CONSTRUCTION</div>
  </div>

  <h1 class="services-title">OUR SERVICES</h1>

  <div class="service" style="left:103px;top:584px">
    <div class="service-badge"><svg viewBox="0 0 44 44"><circle cx="22" cy="22" r="6"/><path d="M22 12v3M22 29v3M12 22h3M29 22h3M15 15l2 2M27 27l2 2M15 29l2-2M27 17l2-2"/><path d="M8 18a15 15 0 0 1 22-11M36 26a15 15 0 0 1-22 11"/><path d="M30 4l0 4-4 0M14 40l0-4 4 0"/></svg></div>
    <div class="service-label">Brewhouse Automation</div>
  </div>
  <div class="service" style="left:275px;top:584px">
    <div class="service-badge"><svg viewBox="0 0 44 44"><path d="M14 6h4v10h-4zM16 16v6H8v6h4v-3h8v-9"/><rect x="26" y="10" width="10" height="28"/><circle cx="31" cy="15" r="2.5"/><path d="M8 38h28"/></svg></div>
    <div class="service-label">Glycol Systems</div>
  </div>
  <div class="service" style="left:448px;top:584px">
    <div class="service-badge"><svg viewBox="0 0 44 44"><rect x="9" y="9" width="10" height="9"/><rect x="25" y="9" width="10" height="9"/><rect x="5" y="21" width="34" height="8" rx="4"/><circle cx="11" cy="25" r="1.6"/><circle cx="17" cy="25" r="1.6"/><circle cx="23" cy="25" r="1.6"/><circle cx="29" cy="25" r="1.6"/><circle cx="35" cy="25" r="1.6"/><path d="M12 29v6M32 29v6M9 35h6M29 35h6"/></svg></div>
    <div class="service-label">Complete Line Design<br>and Install</div>
  </div>

  <div class="service" style="left:17px;top:723px">
    <div class="service-badge"><svg viewBox="0 0 44 44"><path d="M10 6v4l-2 3v9h6v-9l-2-3V6zM20 6v4l-2 3v9h6v-9l-2-3V6zM30 6v4l-2 3v9h6v-9l-2-3V6z"/><rect x="5" y="20" width="34" height="16"/><path d="M5 28h34M14 32h16"/></svg></div>
    <div class="service-label">Packaging Solutions</div>
  </div>
  <div class="service" style="left:189px;top:723px">
    <div class="service-badge"><svg viewBox="0 0 44 44"><path d="M22 6c-3 5-5 7-5 10a5 5 0 0 0 10 0c0-3-2-5-5-10z"/><path d="M4 26h36M8 38l10-12M14 38l10-12M20 38l10-12M26 38l10-12M32 38l6-8"/></svg></div>
    <div class="service-label">Epoxy &amp; Urethane<br>Flooring</div>
  </div>
  <div class="service" style="left:362px;top:723px">
    <div class="service-badge"><svg viewBox="0 0 44 44"><rect x="6" y="16" width="14" height="22"/><path d="M9 20h3M14 20h3M9 25h3M14 25h3M9 30h3M14 30h3"/><rect x="20" y="24" width="8" height="14"/><path d="M30 38V22l6-8-4-4-6 6M36 38h-8M30 34h6"/><circle cx="33" cy="12" r="2"/></svg></div>
    <div class="service-label">New Construction</div>
  </div>
  <div class="service" style="left:534px;top:723px">
    <div class="service-badge"><svg viewBox="0 0 44 44"><circle cx="22" cy="22" r="4"/><circle cx="22" cy="7" r="3"/><circle cx="22" cy="37" r="3"/><circle cx="9" cy="14" r="3"/><circle cx="35" cy="14" r="3"/><circle cx="9" cy="30" r="3"/><circle cx="35" cy="30" r="3"/><path d="M22 10v8M22 26v8M12 15l6 5M32 15l-6 5M12 29l6-5M32 29l-6-5M9 17v10M35 17v10M12 12l7-4M32 12l-7-4"/></svg></div>
    <div class="service-label">Network of Industry<br>Professionals</div>
  </div>

  <div class="contact">
    <div class="contact-line"><span class="contact-icon"><svg viewBox="0 0 10 10"><rect x="1" y="2.5" width="8" height="5"/><path d="M1 2.5l4 3 4-3"/></svg></span>sales@hfwadvisingllc.com</div>
    <div class="contact-line"><span class="contact-icon"><svg viewBox="0 0 10 10"><circle cx="5" cy="5" r="4"/><path d="M1 5h8M5 1c-2 2-2 6 0 8M5 1c2 2 2 6 0 8"/></svg></span>www.harrowfieldpartnersadvisory.com</div>
  </div>
</main>
</body>
</html>
```